Under 13 cricket camp

This is a under 13 cricket camp which is sponsored yearly since 1996
"Home of Leo Brandwick U-13 Cricket Cricket Camp"

1. Look at cricket poster 1....logo in the center with batsman and bowler on the sides.

```html
<!DOCTYPE html>
<html lang="en">
<head>
<meta charset="utf-8">
<title>U-13 Cricket Camp Billboard</title>
<link rel="stylesheet" href="https://fonts.googleapis.com/css2?family=Montserrat:wght@600;700;800&display=swap">
<style>
  :root {
    --pitch-dark: #283224;
    --camp-orange: #e8843a;
    --chalk: #dde3e6;
    --page: #ffffff;
    --photo-sky: #e3e7e5;
    --photo-mid: #c9cfc4;
    --photo-grass: #6f8a55;
  }
  html, body {
    margin: 0;
    width: 1200px;
    height: 1200px;
    overflow: hidden;
    background: var(--page);
  }
  .billboard {
    position: absolute;
    left: 40px;
    top: 321px;
    width: 1448px;
    height: 720px;
    transform: scale(0.7735);
    transform-origin: top left;
    background: var(--pitch-dark);
    font-family: "Montserrat", sans-serif;
    overflow: hidden;
  }
  .billboard-shapes {
    position: absolute;
    inset: 0;
    width: 1448px;
    height: 720px;
  }
  .logo-badge {
    position: absolute;
    left: 126px;
    top: 68px;
    width: 190px;
    height: 70px;
    border-radius: 8px;
    background: var(--pitch-dark);
    color: var(--chalk);
    font-weight: 600;
    font-size: 46px;
    line-height: 70px;
    text-align: center;
    letter-spacing: 1px;
  }
  .headline {
    position: absolute;
    left: 770px;
    width: 660px;
    margin: 0;
    text-align: center;
    text-transform: uppercase;
    white-space: nowrap;
  }
  .headline-intro {
    top: 62px;
    font-weight: 600;
    font-size: 72px;
    color: var(--camp-orange);
    letter-spacing: 1px;
  }
  .headline-name {
    top: 152px;
    font-weight: 800;
    font-size: 66px;
    color: var(--chalk);
  }
  .headline-age {
    top: 228px;
    font-weight: 800;
    font-size: 220px;
    line-height: 1.1;
    color: var(--chalk);
    letter-spacing: -4px;
  }
  .camp-label {
    position: absolute;
    left: 820px;
    top: 478px;
    width: 583px;
    height: 105px;
    line-height: 105px;
    text-align: center;
    font-weight: 800;
    font-size: 62px;
    color: var(--pitch-dark);
    text-transform: uppercase;
  }
</style>
</head>
<body>
  <div class="billboard">
    <svg class="billboard-shapes" viewBox="0 0 1448 720" aria-hidden="false">
      <defs>
        <linearGradient id="photo-tones" x1="0" y1="0" x2="0" y2="1">
          <stop offset="0" stop-color="var(--photo-sky)"/>
          <stop offset="0.45" stop-color="var(--photo-mid)"/>
          <stop offset="1" stop-color="var(--photo-grass)"/>
        </linearGradient>
      </defs>
      <rect class="camp-pill" x="758" y="478" width="645" height="105" rx="22" fill="var(--camp-orange)"/>
      <path class="accent-arc" d="M603,0 C735,60 800,240 785,500" fill="none" stroke="var(--camp-orange)" stroke-width="28"/>
      <path class="team-photo" role="img" aria-label="Photo of young cricketers in whites and a helmet raising gloved hands together in a team high five on a grass field"
            d="M0,0 H603 C722,60 782,240 770,500 L800,720 H0 Z" fill="url(#photo-tones)"/>
    </svg>

    <div class="logo-badge">LOGO</div>

    <p class="headline headline-intro">Home of</p>
    <p class="headline headline-name">Leo Brandwick</p>
    <p class="headline headline-age">U-13</p>
    <div class="camp-label">Cricket Camp</div>
  </div>
</body>
</html>
```